KORBALT

The business want a professional looking business card. We have a scetch we will add but want the extra upgrade, and would like more suggestions for variations of our business cards.

```html
<!DOCTYPE html>
<html lang="en">
<head>
<meta charset="utf-8">
<title>KORBALT – Business Card</title>
<link rel="stylesheet" href="https://fonts.googleapis.com/css2?family=DM+Serif+Display&family=Jost:wght@400;500;600&display=swap">
<style>
  :root {
    --page-bg: #ebecee;
    --card-white: #fbfaf4;
    --ink: #141210;
    --ink-soft: #2a2620;
    --gold: #c9a74f;
    --gold-light: #e6cf8a;
    --gold-mid: #c7a85f;
    --gold-deep: #b18f45;
    --label: #7a7a7a;
  }
  * { box-sizing: border-box; margin: 0; padding: 0; }
  html, body { width: 1200px; height: 1200px; overflow: hidden; }
  body { background: var(--page-bg); position: relative; font-family: "Jost", sans-serif; color: var(--ink); }

  .card { position: absolute; left: 181px; width: 890px; height: 502px; overflow: hidden; }

  /* Front */
  .card-front { top: 85px; background: var(--card-white); }
  .card-front .edge-band { position: absolute; left: 0; right: 0; bottom: 0; height: 14px; background: var(--gold); }
  .brand-lockup { position: absolute; left: 68px; top: 48px; text-align: center; }
  .brand-name { font-family: "DM Serif Display", serif; font-size: 31px; letter-spacing: 0.1em; line-height: 1; color: var(--ink); }
  .brand-sub { font-family: "Jost", sans-serif; font-weight: 600; font-size: 13px; letter-spacing: 0.28em; margin-top: 2px; color: var(--ink); }
  .person-name { position: absolute; left: 72px; top: 150px; font-family: "DM Serif Display", serif; font-size: 49px; letter-spacing: -0.01em; line-height: 1.1; }
  .person-role { position: absolute; left: 75px; top: 215px; font-size: 24px; letter-spacing: 0.1em; color: var(--ink-soft); }
  .divider { position: absolute; left: 74px; top: 270px; width: 551px; height: 2px; background: var(--gold); }
  .contact-list { position: absolute; left: 70px; top: 298px; list-style: none; }
  .contact-item { display: flex; align-items: center; height: 52px; font-size: 27px; color: var(--ink); }
  .contact-icon { width: 38px; height: 38px; margin-right: 29px; flex: none; }

  /* Back */
  .card-back { top: 648px; background: linear-gradient(110deg, var(--gold-light) 0%, var(--gold-mid) 50%, var(--gold-deep) 100%); }
  .back-brand { position: absolute; left: 0; right: 0; top: 190px; text-align: center; font-family: "DM Serif Display", serif; font-size: 78px; letter-spacing: 0.16em; padding-left: 0.16em; line-height: 1; color: var(--ink); }
  .back-tagline { position: absolute; left: 0; right: 0; top: 288px; text-align: center; font-weight: 500; font-size: 30px; letter-spacing: 0.3em; padding-left: 0.3em; color: var(--ink); }
  .corner-ornament { position: absolute; right: 0; bottom: 0; width: 250px; height: 262px;
    background: radial-gradient(circle at 75% 70%, rgba(236, 212, 140, 0.55) 0%, rgba(236, 212, 140, 0.25) 50%, rgba(236, 212, 140, 0) 75%); }

  .side-label { position: absolute; left: 181px; width: 890px; text-align: center; font-size: 20px; letter-spacing: 0.28em; padding-left: 0.28em; color: var(--label); }
  .label-front { top: 606px; }
  .label-back { top: 1170px; }
</style>
</head>
<body>
  <section class="card card-front">
    <div class="brand-lockup">
      <div class="brand-name">KORBALT</div>
      <div class="brand-sub">BRENNVIK</div>
    </div>
    <h1 class="person-name">Anders Lukas Brennvik</h1>
    <p class="person-role">CEO &amp; Founder</p>
    <div class="divider"></div>
    <ul class="contact-list">
      <li class="contact-item">
        <svg class="contact-icon" viewBox="0 0 38 38" aria-hidden="true">
          <rect x="9" y="2" width="18" height="32" rx="3" fill="none" stroke="#c9a74f" stroke-width="3"/>
          <line x1="15" y1="28" x2="21" y2="28" stroke="#c9a74f" stroke-width="2.5" stroke-linecap="round"/>
        </svg>
        004791234567
      </li>
      <li class="contact-item">
        <svg class="contact-icon" viewBox="0 0 38 38" aria-hidden="true">
          <rect x="1" y="8" width="35" height="22" fill="#e2c77c" stroke="#c9a74f" stroke-width="1.5"/>
          <polyline points="1,8 18.5,21 36,8" fill="none" stroke="#fbfaf4" stroke-width="2"/>
        </svg>
        korbalt.llc@postmail.com
      </li>
      <li class="contact-item">
        <svg class="contact-icon" viewBox="0 0 38 38" aria-hidden="true">
          <g fill="none" stroke="#c9a74f" stroke-width="2.5">
            <circle cx="19" cy="19" r="16"/>
            <ellipse cx="19" cy="19" rx="7" ry="16"/>
            <line x1="3" y1="19" x2="35" y2="19"/>
            <line x1="19" y1="3" x2="19" y2="35"/>
            <path d="M6 11h26M6 27h26"/>
          </g>
        </svg>
        www.korbalt.llc
      </li>
    </ul>
    <div class="edge-band"></div>
  </section>
  <p class="side-label label-front">FRONT</p>

  <section class="card card-back">
    <div class="back-brand">KORBALT</div>
    <p class="back-tagline">SINCE 2026</p>
    <div class="corner-ornament" role="img" aria-label="Light gold floral petal ornament in the corner"></div>
  </section>
  <p class="side-label label-back">BACK</p>
</body>
</html>
```